IT Company based on Biology Business Needs a Business Card Design

We need a business card design for a new company called 'Lumen CELL'. We develop the machine learning solutions especially focused on deep learning algorithms for biology industry. Our initial product is a vision detection on biological images to help doctors diagnose the symptoms. We would like to see designs that use the color green.

Industry/Entity Type

Business

```html
<!DOCTYPE html>
<html lang="en">
<head>
<meta charset="utf-8">
<title>Lumen CELL — Business Card</title>
<link rel="stylesheet" href="https://fonts.googleapis.com/css2?family=Questrial&family=Didact+Gothic&display=swap">
<style>
  :root {
    --bg: #ecece8;
    --card: #ffffff;
    --green: #6bbd3f;
    --green-deep: #1f9a4b;
    --green-soft: #a5d47e;
    --text-grey: #6e6e6e;
    --shadow: rgba(0, 0, 0, 0.14);
  }
  * { margin: 0; padding: 0; box-sizing: border-box; }
  html, body {
    width: 1200px;
    height: 950px;
    overflow: hidden;
    background: var(--bg);
  }
  .canvas {
    position: relative;
    width: 1200px;
    height: 950px;
  }
  .card {
    position: absolute;
    width: 630px;
    height: 360px;
    background: var(--card);
    box-shadow: 0 10px 30px var(--shadow);
    overflow: hidden;
  }
  .card-front { left: 90px; top: 80px; }
  .card-back { left: 480px; top: 500px; }

  /* Front */
  .front-brand {
    position: absolute;
    left: 150px;
    top: 142px;
    display: flex;
    align-items: center;
    gap: 18px;
  }
  .brand-dot {
    width: 40px;
    height: 40px;
    border-radius: 50%;
    background: var(--green);
  }
  .brand-name {
    font-family: "Questrial", sans-serif;
    font-size: 50px;
    color: var(--green);
    letter-spacing: -1px;
    line-height: 1;
  }
  .social-row {
    position: absolute;
    right: 34px;
    bottom: 28px;
    display: flex;
    gap: 5px;
  }
  .social-row span {
    width: 22px;
    height: 22px;
    border-radius: 50%;
    background: var(--green);
  }

  /* Back */
  .back-symbol {
    position: absolute;
    left: -120px;
    top: 40px;
    width: 300px;
    height: 300px;
    border-radius: 50%;
    background: radial-gradient(circle at 60% 40%, var(--green-soft), var(--green-deep));
  }
  .back-content {
    position: absolute;
    left: 250px;
    top: 34px;
  }
  .back-brand {
    font-family: "Questrial", sans-serif;
    font-size: 54px;
    color: var(--green);
    letter-spacing: -1px;
    line-height: 1;
    margin-bottom: 16px;
  }
  .person-name {
    font-family: "Didact Gothic", sans-serif;
    font-weight: 700;
    font-size: 20px;
    color: var(--green);
    letter-spacing: 1px;
    text-transform: uppercase;
    -webkit-text-stroke: 0.4px var(--green);
  }
  .person-role {
    font-family: "Didact Gothic", sans-serif;
    font-size: 17px;
    color: var(--green);
    margin-bottom: 12px;
  }
  .address {
    font-family: "Didact Gothic", sans-serif;
    font-size: 16px;
    color: var(--text-grey);
    line-height: 1.3;
    margin-bottom: 10px;
  }
  .contact-list { list-style: none; }
  .contact-list li {
    display: flex;
    align-items: center;
    gap: 12px;
    font-family: "Didact Gothic", sans-serif;
    font-size: 16px;
    color: var(--text-grey);
    line-height: 1.6;
  }
  .contact-icon { width: 14px; height: 14px; flex: none; }
</style>
</head>
<body>
<main class="canvas">

  <section class="card card-front" aria-label="Business card front">
    <div class="front-brand">
      <span class="brand-dot"></span>
      <span class="brand-name">Lumen CELL</span>
    </div>
    <div class="social-row" aria-label="Social profiles">
      <span></span><span></span><span></span><span></span><span></span><span></span>
    </div>
  </section>

  <section class="card card-back" aria-label="Business card back">
    <div class="back-symbol" role="img" aria-label="Brand symbol area"></div>
    <div class="back-content">
      <div class="back-brand">Lumen CELL</div>
      <div class="person-name">Mara Ellison</div>
      <div class="person-role">CEO/Founder</div>
      <address class="address">2143 Fernwood Drive<br>Juneau, Alaska 99801</address>
      <ul class="contact-list">
        <li>
          <svg class="contact-icon" viewBox="0 0 16 16" aria-hidden="true"><path fill="#6bbd3f" d="M3 1l3 3-1.5 2c1 2 3 4 5 5L11.5 9.5l3 3L13 15C7 14 2 9 1 3z"/></svg>
          555 214 7390
        </li>
        <li>
          <svg class="contact-icon" viewBox="0 0 16 16" aria-hidden="true"><rect x="4" y="1" width="8" height="14" rx="1.5" fill="none" stroke="#6bbd3f" stroke-width="1.8"/><circle cx="8" cy="12.5" r="0.9" fill="#6bbd3f"/></svg>
          555 308 6127
        </li>
        <li>
          <svg class="contact-icon" viewBox="0 0 16 16" aria-hidden="true"><rect x="1" y="3" width="14" height="10" rx="1" fill="#6bbd3f"/><path d="M1.5 3.5L8 9l6.5-5.5" fill="none" stroke="#fff" stroke-width="1.3"/></svg>
          hello@lumencell.com
        </li>
        <li>
          <svg class="contact-icon" viewBox="0 0 16 16" aria-hidden="true"><circle cx="8" cy="8" r="6.5" fill="none" stroke="#6bbd3f" stroke-width="1.8"/><path d="M1.5 8h13M8 1.5c-3 3.5-3 9.5 0 13M8 1.5c3 3.5 3 9.5 0 13" fill="none" stroke="#6bbd3f" stroke-width="1.2"/></svg>
          www.lumencell.com
        </li>
      </ul>
    </div>
  </section>

</main>
</body>
</html>
```